Styling of small website for mid-sized Engineering and Manufacturing company

We need the styling for a professional website for a company wich delivers: engineering, manufacturing, assembling, servicing and prototyping. (typically, they produce complex devices in limited series (1-100 pieces. The client comes with an idea and they translate it into design and device).
We have already made a wire-frame, but need a style (colors, fonts, H1, H2, paragraphs, margins, padding etc).
The style must :
- express profession attitude (world of engineering)
- have a fresh, modern look
- be sober (enough (white) space between the elements
The style must also be able to be used in a RWD. At this moment the logo (just letters) uses a green color (#4C6E33), but it isn't an obligation to use the exact same color (even not the 'green' color itself if you think another color is better for the site).
engineering and production
It Company
Coded - Design and coding required
5+ page

```html
<!DOCTYPE html>
<html lang="en">
<head>
<meta charset="utf-8">
<title>Acme – Engineering &amp; Manufacturing</title>
<link rel="stylesheet" href="https://fonts.googleapis.com/css2?family=Roboto:wght@300;400;500&display=swap">
<style>
:root{
  --green:#7bbb1f;
  --ink:#222;
  --text:#555;
  --light-bg:#fafafa;
  --footer:#2b2b2b;
  --footer-bottom:#242424;
  --card-label:#2a2a2a;
  --white:#fff;
}
*{margin:0;padding:0;box-sizing:border-box}
html,body{width:880px;height:1200px;overflow:hidden;background:var(--white)}
body{font-family:'Roboto',Arial,sans-serif;color:var(--text);position:relative}
.abs{position:absolute}

/* header */
.site-header{position:absolute;left:0;top:0;width:880px;height:62px;background:var(--white)}
.logo{position:absolute;left:139px;top:10px;font-size:38px;font-weight:400;color:var(--ink);letter-spacing:.5px;line-height:40px}
.main-nav{position:absolute;top:0;left:402px;height:62px;display:flex;font-size:8.6px;font-weight:400;text-transform:uppercase;color:var(--ink)}
.main-nav a{color:inherit;text-decoration:none;height:62px;line-height:62px;margin-right:22.5px}
.main-nav a.active{background:var(--green);color:var(--white);padding:0 10px;margin-right:15px}
.main-nav a:last-child{margin-right:0}

/* hero */
.hero{position:absolute;left:0;top:62px;width:880px;height:324px;
  background:radial-gradient(ellipse at 45% 55%,#e9b77a 0%,#b9773e 30%,#6d4424 65%,#3d2a1a 100%)}
.hero h1{position:absolute;left:0;width:880px;top:124px;text-align:center;font-size:27.5px;font-weight:300;color:var(--white);letter-spacing:.3px}

/* intro */
.intro h2{position:absolute;left:0;width:880px;top:421px;text-align:center;font-size:18.5px;font-weight:400;color:var(--green)}
.intro p{position:absolute;left:150px;width:580px;top:457px;text-align:center;font-size:10.3px;line-height:16.5px}

/* works */
.works{position:absolute;left:0;top:538px;width:880px;height:265px;background:var(--light-bg)}
.works h2{position:absolute;left:0;width:880px;top:30px;text-align:center;font-size:20.5px;font-weight:400;color:var(--ink)}
.work-card{position:absolute;top:78px;width:138px;height:150px}
.work-photo{height:109px}
.work-label{height:41px;background:var(--card-label);color:var(--white);font-size:11.5px;font-weight:500;text-align:center;line-height:41px;letter-spacing:.2px}

/* showcase */
.section-title{position:absolute;font-size:11.5px;font-weight:400;color:var(--green);text-transform:uppercase;line-height:16.5px}
.client-box{position:absolute;left:140px;top:878px;width:164px;height:124px;background:#f0f0f0;display:flex;align-items:center;justify-content:center}
.client-name{font-size:16px;font-weight:500;color:#1d5a7a}
.showcase-text{position:absolute;left:320px;top:874px;width:240px;font-size:10.3px;line-height:16.4px}
.reasons{position:absolute;left:590px;top:886px;list-style:none;font-size:10.3px}
.reasons li{height:20px;display:flex;align-items:center}
.reasons svg{margin-right:8px}

/* footer */
.site-footer{position:absolute;left:0;top:1039px;width:880px;height:122px;background:var(--footer);color:var(--white)}
.footer-col{position:absolute;top:26px}
.footer-col h3{font-size:11.5px;font-weight:400;text-transform:uppercase;margin-bottom:9px;letter-spacing:.2px}
.footer-col p{font-size:9px;line-height:15px}
.map-btn{display:inline-flex;align-items:center;margin-top:9px;height:20px;padding:0 8px;background:#1b1b1b;color:var(--white);font-size:8.3px;text-decoration:none;gap:6px}
.footer-bottom{position:absolute;left:0;top:1161px;width:880px;height:39px;background:var(--footer-bottom);color:#ddd;font-size:8.6px;text-align:center;line-height:39px}
</style>
</head>
<body>

<header class="site-header">
  <div class="logo">LOGO</div>
  <nav class="main-nav">
    <a class="active" href="#">Home</a>
    <a href="#">Services</a>
    <a href="#">Portfolio</a>
    <a href="#">News</a>
    <a href="#">About Acme</a>
    <a href="#">Contact</a>
  </nav>
</header>

<section class="hero" role="img" aria-label="Close-up of an angle grinder cutting metal with sparks flying">
  <h1>ENGINEERING &amp; MANUFACTURING</h1>
</section>

<section class="intro">
  <h2>TECHNOLOGICAL SOLUTION IDEA TO PRODUCT</h2>
  <p>Acme ontwerpt en fabriceert to estellen voor de meest uniteenlopende industrieen. Met als belangrijkste de (para) medische sector. Onze Oplossingen zijn even veelzildig als de vragen van onze klanten. Engineering, prototype, (serie) productie en service onder een dak. Dat maakt het traject van vraag naar opplossing sneller en beter beheersbaar.</p>
</section>

<section class="works">
  <h2>OUR WORKS</h2>
  <div class="work-card" style="left:140px">
    <div class="work-photo" role="img" aria-label="Engineers reviewing documents in a workshop" style="background:linear-gradient(160deg,#d8dcd8,#8a8f86 60%,#5f6a58)"></div>
    <div class="work-label">ENGINEERING</div>
  </div>
  <div class="work-card" style="left:295px">
    <div class="work-photo" role="img" aria-label="CNC machine milling a metal prototype part" style="background:linear-gradient(160deg,#e4e6ea,#7e838c 55%,#2d2f33)"></div>
    <div class="work-label">PROTOTYPING</div>
  </div>
  <div class="work-card" style="left:450px">
    <div class="work-photo" role="img" aria-label="Technician assembling a machine on a production floor" style="background:linear-gradient(160deg,#4a6a3a,#3b4650 55%,#b59a3d)"></div>
    <div class="work-label">ASSEMBLEREN</div>
  </div>
  <div class="work-card" style="left:604px">
    <div class="work-photo" role="img" aria-label="Welder working on metal with bright sparks" style="background:linear-gradient(160deg,#2d4f8a,#3b4a6e 50%,#b9b4c8)"></div>
    <div class="work-label">SERVICING</div>
  </div>
</section>

<section class="showcase">
  <h3 class="section-title" style="left:140px;top:849px">SHOWCASE CLIENT X</h3>
  <div class="client-box"><span class="client-name">Northfield Grid</span></div>
  <p class="showcase-text">Lorem ipsum dolor sit amet, consectetur adipiscing elit. Nulla quam velit, vulputate eu pharetra nec, mattis ac neque. Duis vulputate commodo lectus, ac blandit elit tincidunt id. Sed rhoncus, tortor sed eleifend tristique, tortor mauris molestie elit, et lacinia ipsum quam nec dui. Quisque nec mauric sit amet elit iaculis pretium sit amet quis magna. Aenean velit odio, elementum in tempus ut, vehicula eu diam.</p>

  <h3 class="section-title" style="left:590px;top:849px;width:160px">WAAROM KLANTEN VOOR ONS KIEZEN</h3>
  <ul class="reasons">
    <li><svg width="8" height="8" viewBox="0 0 8 8"><circle cx="4" cy="4" r="4" fill="#7bbb1f"/><path d="M2.2 4.1 3.5 5.3 5.9 2.8" stroke="#fff" stroke-width="1.1" fill="none"/></svg>Al 4.251 abonnees</li>
    <li><svg width="8" height="8" viewBox="0 0 8 8"><circle cx="4" cy="4" r="4" fill="#7bbb1f"/><path d="M2.2 4.1 3.5 5.3 5.9 2.8" stroke="#fff" stroke-width="1.1" fill="none"/></svg>1 keer per maand</li>
    <li><svg width="8" height="8" viewBox="0 0 8 8"><circle cx="4" cy="4" r="4" fill="#7bbb1f"/><path d="M2.2 4.1 3.5 5.3 5.9 2.8" stroke="#fff" stroke-width="1.1" fill="none"/></svg>Exclusieve tips en promo’s</li>
    <li><svg width="8" height="8" viewBox="0 0 8 8"><circle cx="4" cy="4" r="4" fill="#7bbb1f"/><path d="M2.2 4.1 3.5 5.3 5.9 2.8" stroke="#fff" stroke-width="1.1" fill="none"/></svg>Al 4.251 abonnees</li>
    <li><svg width="8" height="8" viewBox="0 0 8 8"><circle cx="4" cy="4" r="4" fill="#7bbb1f"/><path d="M2.2 4.1 3.5 5.3 5.9 2.8" stroke="#fff" stroke-width="1.1" fill="none"/></svg>1 keer per maand</li>
    <li><svg width="8" height="8" viewBox="0 0 8 8"><circle cx="4" cy="4" r="4" fill="#7bbb1f"/><path d="M2.2 4.1 3.5 5.3 5.9 2.8" stroke="#fff" stroke-width="1.1" fill="none"/></svg>Exclusieve tips en promo’s</li>
  </ul>
</section>

<footer class="site-footer">
  <div class="footer-col" style="left:140px">
    <h3>Contact us</h3>
    <p>Email: info@acmeworks.nl<br>Phone: 0240123456</p>
  </div>
  <div class="footer-col" style="left:357px">
    <h3>Our slaes department</h3>
    <p>Street: xxx<br>xxx City</p>
    <a class="map-btn" href="#">View Map <svg width="14" height="10" viewBox="0 0 14 10"><path d="M1 1l4 4-4 4M7 1l4 4-4 4" stroke="#fff" stroke-width="2" fill="none"/></svg></a>
  </div>
  <div class="footer-col" style="left:614px">
    <h3>R&amp;D and production</h3>
    <p>Street: xxx<br>xxx City2</p>
    <a class="map-btn" href="#">View Map <svg width="14" height="10" viewBox="0 0 14 10"><path d="M1 1l4 4-4 4M7 1l4 4-4 4" stroke="#fff" stroke-width="2" fill="none"/></svg></a>
  </div>
</footer>
<div class="footer-bottom">Copyright © 2015 ACMEWORKS.nl. All rights reserved</div>

</body>
</html>
```